Business Card Design Project

Business card design for an IT Service company. A logo has already been created in a different contest and has been attached to this project. Ideally we're looking for a double sided business card that matches the look and feel of our newly created logo.

We're open to creativity if you feel a tag line is needed such as "IT Services and Application Development". We're open to really and look and feel - even single sided business cards if you feel you have something that's a great idea.

Last thought here - I'm not sure how it'll look but maybe a two tone card? One side dark blue and the other side white? Don't limit the design submissions to this tho - just curious if it would look good

Nothing too busy please - simple... Thank you and happy designing!

Target Market(s)

Businesses that require IT Services and support for hosted services, technical consultation, web design.

Industry/Entity Type

Business

Font styles to use
Sans Serif

Requirements
Must have
• Use the colors provided in the logo (see attachment) or additional colors that compliment
Must have the following contact info (not necessarily in this order):
- Alan Fisk
- Founding Partner
- afisk@quillbarrow.example
- 555-382-1946
- www.quillbarrow.example

```html
<!DOCTYPE html>
<html lang="en">
<head>
<meta charset="utf-8">
<title>Quillbarrow Business Card</title>
<link rel="stylesheet" href="https://fonts.googleapis.com/css2?family=Open+Sans:wght@400;600;700&display=swap">
<style>
  :root {
    --canvas-bg: #b9b9b9;
    --card-white: #ffffff;
    --navy: #17254a;
    --navy-deep: #111c3a;
    --brand-blue: #1f6fb5;
    --brand-green: #6aa63a;
    --ink: #222222;
    --silver: #d3d6dc;
    --tagline-grey: #9aa3b5;
  }
  * { box-sizing: border-box; margin: 0; padding: 0; }
  html, body { width: 1200px; height: 900px; overflow: hidden; }
  body {
    background: var(--canvas-bg);
    font-family: "Open Sans", Arial, sans-serif;
    display: flex;
    align-items: center;
    justify-content: center;
    gap: 40px;
  }
  .card {
    position: relative;
    width: 540px;
    height: 310px;
    border-radius: 22px;
    overflow: hidden;
  }
  /* Front */
  .card-front { background: var(--card-white); }
  .brand {
    position: absolute;
    left: 30px;
    top: 44px;
    display: flex;
    align-items: center;
    gap: 16px;
  }
  .brand-square {
    width: 58px;
    height: 58px;
    background: var(--brand-green);
  }
  .brand-name {
    font-size: 46px;
    font-weight: 700;
    color: var(--navy);
    letter-spacing: -0.5px;
  }
  .tagline-band {
    position: absolute;
    left: 0;
    right: 0;
    top: 134px;
    height: 20px;
    background: var(--navy);
    color: #ffffff;
    font-size: 12.5px;
    letter-spacing: 3.6px;
    line-height: 20px;
    padding-left: 22px;
    white-space: nowrap;
  }
  .person {
    position: absolute;
    left: 24px;
    top: 160px;
  }
  .person-name {
    font-size: 19px;
    font-weight: 700;
    color: var(--brand-blue);
    line-height: 1.2;
  }
  .person-title {
    font-size: 12px;
    color: var(--ink);
  }
  .contacts {
    position: absolute;
    left: 24px;
    top: 222px;
    list-style: none;
  }
  .contacts li {
    display: flex;
    align-items: center;
    gap: 4px;
    font-size: 13.5px;
    color: var(--ink);
    line-height: 19px;
  }
  .contacts svg { width: 13px; height: 13px; fill: var(--brand-blue); }
  /* Back */
  .card-back {
    background: radial-gradient(ellipse at 50% 40%, #22325c 0%, var(--navy) 55%, var(--navy-deep) 100%);
    display: flex;
    flex-direction: column;
    align-items: center;
    justify-content: center;
    gap: 8px;
  }
  .back-brand {
    display: flex;
    align-items: center;
    gap: 16px;
  }
  .back-brand .brand-square { width: 60px; height: 60px; }
  .back-brand .brand-name { color: var(--silver); font-size: 44px; }
  .back-tagline {
    font-size: 11.5px;
    letter-spacing: 3px;
    color: var(--tagline-grey);
    font-weight: 600;
    white-space: nowrap;
  }
</style>
</head>
<body>
  <section class="card card-front" aria-label="Card front">
    <div class="brand">
      <span class="brand-square"></span>
      <span class="brand-name">Quillbarrow</span>
    </div>
    <div class="tagline-band">IT Services and Application Development</div>
    <div class="person">
      <p class="person-name">Alan Fisk</p>
      <p class="person-title">Founding Partner</p>
    </div>
    <ul class="contacts">
      <li>
        <svg viewBox="0 0 24 24" aria-hidden="true"><path d="M6.6 10.8a15.1 15.1 0 0 0 6.6 6.6l2.2-2.2a1 1 0 0 1 1-.25 11.4 11.4 0 0 0 3.6.57 1 1 0 0 1 1 1V20a1 1 0 0 1-1 1A17 17 0 0 1 3 4a1 1 0 0 1 1-1h3.5a1 1 0 0 1 1 1c0 1.25.2 2.45.57 3.57a1 1 0 0 1-.25 1z"/></svg>
        555-382-1946
      </li>
      <li>
        <svg viewBox="0 0 24 24" aria-hidden="true"><path d="M12 2a10 10 0 1 0 0 20 10 10 0 0 0 0-20zm6.9 6h-2.9a15.7 15.7 0 0 0-1.4-3.6A8 8 0 0 1 18.9 8zM12 4c.8 1.2 1.5 2.5 1.9 4h-3.8c.4-1.5 1.1-2.8 1.9-4zM4.3 14a8 8 0 0 1 0-4h3.4a16.5 16.5 0 0 0 0 4zm.8 2h2.9c.3 1.3.8 2.5 1.4 3.6A8 8 0 0 1 5.1 16zM8 8H5.1a8 8 0 0 1 4.3-3.6C8.8 5.5 8.3 6.7 8 8zm4 12c-.8-1.2-1.5-2.5-1.9-4h3.8c-.4 1.5-1.1 2.8-1.9 4zm2.3-6H9.7a14.7 14.7 0 0 1 0-4h4.6a14.7 14.7 0 0 1 0 4zm.3 5.6c.6-1.1 1.1-2.3 1.4-3.6h2.9a8 8 0 0 1-4.3 3.6zm1.7-5.6a16.5 16.5 0 0 0 0-4h3.4a8 8 0 0 1 0 4z"/></svg>
        www.quillbarrow.example
      </li>
      <li>
        <svg viewBox="0 0 24 24" aria-hidden="true"><path d="M3 5h18a1 1 0 0 1 1 1v12a1 1 0 0 1-1 1H3a1 1 0 0 1-1-1V6a1 1 0 0 1 1-1zm1 2.4V17h16V7.4l-8 5.3z M5 7l7 4.6L19 7z"/></svg>
        afisk@quillbarrow.example
      </li>
    </ul>
  </section>

  <section class="card card-back" aria-label="Card back">
    <div class="back-brand">
      <span class="brand-square"></span>
      <span class="brand-name">Quillbarrow</span>
    </div>
    <p class="back-tagline">IT Services and Application Development</p>
  </section>
</body>
</html>
```